Tri-fold Brochure Design for Law Firm

I need a tri-fold brochure to give to prospective clients.
I have attached a Photoshop design file of a tri-fold brochure. The content (copy) is good, however, he brochure itself looks very amateurish.
I want a professional, sophisticated looking brochure.
The law firm specializes in commercial debt collection.
The law firm is located in New York City.
Our target market is business owners, doctors, lawyers, collection agencies and accountants.
Visit my website which is being designed at www.dorvenlaw.com. I like the font used for the name of my company and the rich blue color used.

Target Market(s)

Business Owners, Doctors, Law Firms and Accountants

Industry/Entity Type

Law Firm

Font styles to use
Serif

Requirements
Must have
• Professional quality graphic work. Attention to details.
• PHOTOGRAPHS ONLY, NO CLIP-ART.
• DARK COLORS - NAVY BLUE, HUNTER GREEN, BLACK, GRAY & WHITE
Nice to have
• I want it to look smart, modern and sophisticated.
• Visit my website which is being designed at www.dorvenlaw.com. I like the font used for the name of my company and the rich blue color used.
Should not have
• Bad artwork
• CLIP ART

```html
<!DOCTYPE html>
<html lang="en">
<head>
<meta charset="utf-8">
<title>Dorven &amp; Associates — Tri-fold Brochure Interior</title>
<link rel="stylesheet" href="https://fonts.googleapis.com/css2?family=Marcellus&family=Marcellus+SC&family=Source+Sans+3:wght@400;600;700&display=swap">
<style>
  :root {
    --page-bg: #e9e6e1;
    --panel-gray: #4a4947;
    --panel-charcoal: #2a2a2b;
    --box-dark: rgba(52, 56, 60, 0.88);
    --box-edge: rgba(200, 225, 238, 0.55);
    --accent-blue: #5ea9d6;
    --text-light: #e6e6e4;
    --photo-deep: #1f5f86;
    --photo-mid: #3d8fbd;
    --photo-light: #a8d6ea;
  }
  * { box-sizing: border-box; margin: 0; padding: 0; }
  html, body { width: 1200px; height: 900px; overflow: hidden; }
  body {
    background: var(--page-bg);
    font-family: "Source Sans 3", sans-serif;
    color: var(--text-light);
  }
  .brochure {
    position: absolute;
    left: 50px; top: 25px;
    width: 1100px; height: 850px;
    display: flex;
  }
  .panel { position: relative; width: 366.66px; height: 100%; overflow: hidden; }
  .panel p { font-size: 12px; line-height: 1.38; text-align: justify; margin-bottom: 9px; }

  /* Left panel */
  .panel--intro { background: var(--panel-gray); }
  .panel--intro .panel-copy { padding: 44px 34px 0; }
  .section-title {
    font-family: "Marcellus", serif;
    font-weight: 400;
    color: var(--accent-blue);
    font-size: 24px;
    text-align: center;
    letter-spacing: 0.5px;
    margin: 6px 0 12px;
  }
  .intro-lead { text-align: center !important; }
  .firm-name { font-weight: 700; text-transform: uppercase; letter-spacing: 0.3px; }
  .intro-photo {
    position: absolute; left: 0; bottom: 0; width: 100%; height: 170px;
    background: linear-gradient(100deg, #cfe7f2 0%, #6fb2d6 28%, #2f6f96 55%, #5a9cc4 78%, #c5e3f0 100%);
  }

  /* Middle panel */
  .panel--services { background: var(--photo-deep); }
  .services-photo {
    position: absolute; inset: 0;
    background:
      linear-gradient(90deg, rgba(255,255,255,0) 0%, rgba(200,235,248,0.35) 50%, rgba(255,255,255,0) 100%),
      linear-gradient(180deg, var(--photo-light) 0%, var(--photo-mid) 35%, var(--photo-deep) 70%, #9fcfe4 100%);
  }
  .info-box {
    position: absolute; left: 34px; right: 34px;
    background: var(--box-dark);
    border: 1px solid var(--box-edge);
    padding: 16px 20px 12px;
  }
  .info-box--fees { top: 92px; height: 222px; }
  .info-box--medical { top: 336px; height: 440px; }
  .box-title {
    font-family: "Marcellus", serif;
    color: var(--accent-blue);
    font-size: 17px;
    text-align: center;
    margin-bottom: 10px;
  }
  .fee-list { list-style: none; font-size: 12px; line-height: 1.4; }
  .fee-list li::before { content: "• "; }

  /* Right panel */
  .panel--advisory { background: var(--panel-charcoal); }
  .panel--advisory .panel-copy { padding: 58px 30px 0; }
  .advisory-title {
    font-family: "Marcellus SC", serif;
    color: var(--accent-blue);
    font-size: 16px;
    letter-spacing: 0.6px;
    margin: 4px 0 4px;
  }
  .advisory-question { text-align: left !important; }
</style>
</head>
<body>
<main class="brochure">

  <section class="panel panel--intro">
    <div class="panel-copy">
      <h2 class="section-title">Who We Are</h2>
      <p class="intro-lead"><span class="firm-name">Dorven &amp; Associates, PLLC ("Dorven")</span> is a New York based law firm devoted to the collection of accounts receivable and business debts.</p>

      <h2 class="section-title">What We Do</h2>
      <p>Within 24 to 72 hours of receiving a claim, we will verify the debtor, investigate the debtor's ability to pay, contact all known stakeholders and the debtor with the intent of collecting the full amount due in the shortest time possible.</p>
      <p>We will use all legal means necessary to locate debtors, seize or otherwise garnish a debtor's assets and income, while always having an ultimate goal of obtaining an amicable resolution as quickly as possible.</p>

      <h2 class="section-title">Our Mission</h2>
      <p>Our mission is to protect our clients' bottom line while preserving their reputation.</p>
      <p>We recognize and appreciate that your Debtor was once a trusted customer and may be a source of future revenue.</p>
      <p>We treat all Debtors with respect, while aggressively seeking to collect all monies owed.</p>
    </div>
    <div class="intro-photo" role="img" aria-label="Photograph of a judge's gavel and scales of justice in blue tones"></div>
  </section>

  <section class="panel panel--services">
    <div class="services-photo" role="img" aria-label="Abstract blue photograph of glass columns"></div>

    <article class="info-box info-box--fees">
      <h3 class="box-title">Flexible Fee Structure</h3>
      <p>We recognize that each claim is unique, therefore, to better serve our clients we offer a variety of fee structures that meet the needs of our clients, including:</p>
      <ul class="fee-list">
        <li>Contingency Fee</li>
        <li>Flat Fee</li>
        <li>Hourly Fee</li>
        <li>Monthly or Annual Retainer</li>
        <li>Any combination of the above</li>
      </ul>
    </article>

    <article class="info-box info-box--medical">
      <h3 class="box-title">Handling Medical Receivables</h3>
      <p>Medical receivables require a soft touch.</p>
      <p>Doctors and health organizations often write-off tens of thousands of dollars in unpaid deductibles and co-insurance which are rightfully due them, out of fear that pursuing these debts will alienate, upset or offend their patients.</p>
      <p>We offer non-legal, HIPPA compliant collection methods which can effectively and consistently turn these otherwise uncollectible assets into real cash.</p>
      <p>Using a combination of letters and phone calls, our staff contacts patients in a professional and friendly manner to arrange for payments as small as $15 per month, encouraging them to pay all monies owed.</p>
    </article>
  </section>

  <section class="panel panel--advisory">
    <div class="panel-copy">
      <h3 class="advisory-title">Credit Advisory Services</h3>
      <p class="advisory-question">How well do you really know your customers?</p>
      <p>As an added service to all of our clients, we will draft a customized credit application to be distributed to all of their customers.</p>
      <p>Working closely and alongside their salespeople, we will discretely review and verify the customers' information and investigate all known stakeholders in order to determine creditworthiness.</p>
      <p>As your credit advisor, we will then make a meaningful recommendation with regard to the amount and terms credit should be offered to specific customers. Once a credit determination is made, we can provide the client with a credit agreement detailing each parties' obligations. Using such agreements minimizes risk, while enhancing our clients' professional stature with their customers.</p>

      <h3 class="advisory-title">Keeping You In Compliance</h3>
      <p>As your collection attorney and advisor, we will assure that your collection practices are in full compliance with all applicable Federal and State laws, including The Fair Debt Collection Practices Act (FDCPA) and The Health Insurance Portability and Accountability Act (HIPPA).</p>

      <h3 class="advisory-title">State-Of-The-Art Technology</h3>
      <p>Our firm prides itself on utilizing the state-of-the-art technology in law office management, telephony, cyber security, document production, and cloud storage. Our clients can be assured that their critical business data is stored in a safe, secure, and confidential environment, while allowing us to seamlessly handle a large and ever growing book of business in a timely manner.</p>
    </div>
  </section>

</main>
</body>
</html>
```